Business Cards

Business card design for my company.
I would like the card's background colour to be black. You can also see our web site to get an idea of our brand. https://www.dlqmarrowfield.com.au/
- Name
- Email

```html
<!DOCTYPE html>
<html lang="en">
<head>
<meta charset="utf-8">
<title>DLQ Marrowfield – Business Cards</title>
<link href="https://fonts.googleapis.com/css2?family=Montserrat:wght@400;500;700;800&display=swap" rel="stylesheet">
<style>
  :root {
    --stage: #141414;
    --card-dark: #1e1e1e;
    --card-back: #1a1a1a;
    --brand-green: #0f9a45;
    --ink-dark: #1b1b1b;
    --text-light: #f2f2f2;
  }
  * { margin: 0; padding: 0; box-sizing: border-box; }
  html, body {
    width: 1200px; height: 800px; overflow: hidden;
    background: var(--stage);
    font-family: "Montserrat", sans-serif;
  }
  .stage {
    width: 1200px; height: 800px;
    display: flex; align-items: center; justify-content: center; gap: 40px;
  }
  .card {
    position: relative;
    width: 560px; height: 320px;
    border-radius: 18px;
    overflow: hidden;
    box-shadow: inset 0 -4px 0 var(--brand-green);
  }
  .card--front { background: var(--card-dark); }
  .card--back { background: var(--card-back); }

  .front-band { position: absolute; inset: 0; }

  .holder {
    position: absolute; right: 36px; top: 22px; text-align: right;
    color: var(--ink-dark);
  }
  .holder__name { font-weight: 800; font-size: 27px; letter-spacing: 1.5px; }
  .holder__title { font-weight: 400; font-size: 14px; margin-top: 2px; letter-spacing: 0.5px; }

  .brand {
    position: absolute; left: 48px; top: 104px;
    display: flex; align-items: center; gap: 10px;
  }
  .brand__mark { width: 14px; height: 14px; background: var(--brand-green); }
  .brand__name {
    color: var(--text-light); font-weight: 800; font-size: 22px;
    line-height: 1.1; letter-spacing: 2px;
  }

  .contacts {
    position: absolute; left: 60px; top: 186px;
    list-style: none; color: var(--text-light);
    font-size: 14px; font-weight: 500;
  }
  .contacts li { display: flex; align-items: center; gap: 12px; height: 26px; }
  .contacts svg { width: 14px; height: 14px; fill: var(--brand-green); flex: none; }

  .back-pattern {
    position: absolute; inset: 0 0 4px 0;
    background: linear-gradient(135deg, #262626 0%, #1c1c1c 55%, #151515 100%);
  }
  .back-brand {
    position: absolute; right: 40px; bottom: 44px;
    display: flex; align-items: center; gap: 6px;
  }
  .back-brand__mark { width: 8px; height: 8px; background: var(--brand-green); }
  .back-brand__name {
    color: var(--text-light); font-weight: 800; font-size: 11px; letter-spacing: 1px;
  }
</style>
</head>
<body>
<main class="stage">
  <section class="card card--front">
    <svg class="front-band" viewBox="0 0 560 320" width="560" height="320">
      <path d="M0,0 H560 V80 H236 L210,62 H150 L30,92 H0 Z" fill="var(--brand-green)"/>
      <path d="M0,101 H32 L150,71 H208 L234,89 H560" fill="none" stroke="var(--brand-green)" stroke-width="3"/>
    </svg>

    <div class="holder">
      <div class="holder__name">TOM ELLERY</div>
      <div class="holder__title">General Manager</div>
    </div>

    <div class="brand">
      <span class="brand__mark"></span>
      <span class="brand__name">DLQ<br>MARROWFIELD</span>
    </div>

    <ul class="contacts">
      <li>
        <svg viewBox="0 0 24 24"><path d="M6.6 10.8a15.1 15.1 0 0 0 6.6 6.6l2.2-2.2c.3-.3.7-.4 1-.2 1.1.4 2.3.6 3.6.6.6 0 1 .4 1 1V20c0 .6-.4 1-1 1C10.6 21 3 13.4 3 4c0-.6.4-1 1-1h3.5c.6 0 1 .4 1 1 0 1.3.2 2.5.6 3.6.1.3 0 .7-.2 1z"/></svg>
        0400 555 018
      </li>
      <li>
        <svg viewBox="0 0 24 24"><path d="M2 5h20v14H2z M3 6l9 7 9-7" fill="none" stroke="var(--brand-green)" stroke-width="2"/></svg>
        info@dlqmarrowfield.com.au
      </li>
      <li>
        <svg viewBox="0 0 24 24"><circle cx="12" cy="12" r="9" fill="none" stroke="var(--brand-green)" stroke-width="2"/><path d="M3 12h18M12 3c3 3 3 15 0 18M12 3c-3 3-3 15 0 18" fill="none" stroke="var(--brand-green)" stroke-width="1.6"/></svg>
        dlqmarrowfield.com.au
      </li>
      <li>
        <svg viewBox="0 0 24 24"><path d="M12 2a7 7 0 0 0-7 7c0 5 7 13 7 13s7-8 7-13a7 7 0 0 0-7-7zm0 9.5A2.5 2.5 0 1 1 12 6.5a2.5 2.5 0 0 1 0 5z"/></svg>
        Kelverton, Tasmania, Australia
      </li>
    </ul>
  </section>

  <section class="card card--back">
    <div class="back-pattern" role="img" aria-label="Dark embossed repeating brand pattern"></div>
    <div class="back-brand">
      <span class="back-brand__mark"></span>
      <span class="back-brand__name">DLQ MARROWFIELD</span>
    </div>
  </section>
</main>
</body>
</html>
```